Medical equipment business looking for professional, unique business card

We need a business card design for a durable medical equipment company. We are small but would like our cards to express that we are much bigger. We focus on braces (back, knee, wrist, etc) but also do crutches, rollators, wheelchairs- basically medical equipment that gets you going and back in Action. Our colors are blue and green and our logo has an arrow and use of a "spine". We'd like to express professionalism while being unique.

Industry/Entity Type

Medical Equipment

Contact Information for Business Card

Professional feel but unique. Memorable.

Font styles to use
Serif
Sans Serif
Other font styles liked:
• verdana

Requirements
Must have
• card holders cell#, business phone#, fax#, email, website address, business address, logo
Nice to have
• use of medical/healthcare related descriptive words, items, look
Should not have
• the wrong colors or cartoon characters.

```html
<!DOCTYPE html>
<html lang="en">
<head>
<meta charset="utf-8">
<title>Stride Medical – Business Card</title>
<link rel="stylesheet" href="https://fonts.googleapis.com/css2?family=Source+Sans+3:wght@400;600;700&display=swap">
<style>
  :root {
    --bg: #eef0f2;
    --white: #f7f8f8;
    --green: #8cc63f;
    --blue: #0d5d98;
    --blue-deep: #0a4c80;
    --cyan: #2bb3e0;
    --text-light: #ffffff;
    --shadow: rgba(10, 40, 70, 0.22);
  }
  * { box-sizing: border-box; margin: 0; padding: 0; }
  html, body { width: 1200px; height: 780px; overflow: hidden; }
  body {
    background: var(--bg);
    font-family: "Source Sans 3", Verdana, sans-serif;
    display: flex;
    align-items: center;
    justify-content: center;
    gap: 40px;
  }
  .card {
    width: 540px;
    height: 310px;
    border-radius: 18px;
    overflow: hidden;
    box-shadow: 0 10px 24px var(--shadow);
    position: relative;
  }

  /* Front */
  .card-front { background: var(--blue); display: flex; flex-direction: column; }
  .front-top {
    height: 122px;
    background: var(--white);
    display: flex;
    flex-direction: column;
    justify-content: center;
    padding-left: 64px;
  }
  .brand-band { height: 14px; background: var(--green); }
  .front-body {
    flex: 1;
    background: linear-gradient(180deg, var(--blue) 0%, var(--blue-deep) 100%);
    padding: 12px 64px 0;
    color: var(--text-light);
  }
  .wordmark {
    display: flex;
    align-items: center;
    gap: 10px;
    font-weight: 600;
    font-size: 38px;
    line-height: 1;
    color: var(--blue);
    letter-spacing: -0.5px;
  }
  .wordmark-dot {
    width: 12px; height: 12px;
    border-radius: 50%;
    background: var(--green);
  }
  .descriptor {
    margin-top: 6px;
    margin-left: 22px;
    font-size: 13px;
    font-weight: 600;
    color: var(--cyan);
  }
  .holder { font-size: 17px; line-height: 1.2; display: flex; align-items: center; gap: 8px; }
  .holder-name { font-weight: 700; color: var(--green); letter-spacing: 0.5px; text-transform: uppercase; }
  .holder-divider { width: 1px; height: 16px; background: var(--cyan); }
  .holder-role { color: var(--cyan); font-weight: 400; }
  .contact { margin-top: 9px; font-size: 14px; line-height: 1.4; }
  .contact b { font-weight: 700; }
  .address { margin-top: 9px; font-size: 14px; line-height: 1.4; }

  /* Back */
  .card-back {
    background: radial-gradient(ellipse at 40% 40%, #11679f 0%, var(--blue) 45%, var(--blue-deep) 100%);
    display: flex;
    flex-direction: column;
    justify-content: center;
    padding-left: 120px;
  }
  .card-back .wordmark { color: var(--text-light); font-size: 46px; }
  .card-back .descriptor { font-size: 15px; margin-left: 22px; }
  .website {
    margin-top: 26px;
    margin-left: 22px;
    font-size: 14px;
    color: var(--text-light);
    letter-spacing: 0.3px;
  }
</style>
</head>
<body>
  <section class="card card-front">
    <div class="front-top">
      <div class="wordmark"><span class="wordmark-dot"></span>Stride Medical</div>
      <div class="descriptor">Durable Medical Equipment</div>
    </div>
    <div class="brand-band"></div>
    <div class="front-body">
      <div class="holder">
        <span class="holder-name">Dana Reyes</span>
        <span class="holder-divider"></span>
        <span class="holder-role">Director</span>
      </div>
      <div class="contact">
        <div><b>P:</b> (02) 5550 1847</div>
        <div><b>C:</b> (02) 5550 2963</div>
        <div><b>F:</b> (02) 5550 1848</div>
        <div>hello@stridemedical.com</div>
      </div>
      <div class="address">PO BOX 456 Elm Avenue, 3rd street USA</div>
    </div>
  </section>

  <section class="card card-back">
    <div class="wordmark"><span class="wordmark-dot"></span>Stride Medical</div>
    <div class="descriptor">Durable Medical Equipment</div>
    <div class="website">www.stridemedical.com</div>
  </section>
</body>
</html>
```